Tiling Service Contractor For Custom Van Design.

I am a independent Tiling Contractor
All types of tiles, Ceramic, Porcelain, Natural Stone,
I need my van to be designed to give maximum advertising to generate more buisness and leads. I am in 2 minds, weather to have something brief and professional or go for the full wrap, I am open to all designs, you don necessary have to use my logo, as i have seen other independent contractors
Domestic & Commercial
Walls & Floor Tiler
Complete Bathroom Installations
www.kelvanwork.ie
Email: info@kelvanwork.ie

Target Market(s)

Everybody, house owners, other contractors

Industry/Entity Type

construction, tiling, building

Requirements
Must have
• contact info

```html
<!DOCTYPE html>
<html lang="en">
<head>
<meta charset="utf-8">
<title>Kelvan Work – Van Wrap Layout</title>
<link href="https://fonts.googleapis.com/css2?family=Montserrat:wght@500;600;700;800&display=swap" rel="stylesheet">
<style>
  :root{
    --ground:#e9e9ea;
    --panel:#ffffff;
    --ink:#111113;
    --band-dark:#1d1d20;
    --band-grey:#8c8c90;
    --text-grey:#7a7a7e;
    --paper:#ffffff;
  }
  *{box-sizing:border-box;margin:0;padding:0}
  html,body{width:770px;height:1200px;overflow:hidden;background:var(--ground)}
  body{position:relative;font-family:"Montserrat",sans-serif}
  .view{position:absolute;overflow:hidden}
  .view svg{display:block;width:100%;height:100%}
  .view--side-left{left:0;top:0;width:770px;height:415px}
  .view--side-right{left:0;top:415px;width:770px;height:385px}
  .view--front{left:0;top:800px;width:372px;height:400px}
  .view--rear{left:374px;top:800px;width:396px;height:400px}
  .divider{position:absolute;background:var(--paper)}
  .divider--h1{left:0;top:414px;width:770px;height:2px}
  .divider--h2{left:0;top:799px;width:770px;height:2px}
  .divider--v{left:372px;top:800px;width:2px;height:400px}

  svg text{font-family:"Montserrat",sans-serif}
  .panel{fill:var(--panel)}
  .band-dark{fill:var(--band-dark)}
  .band-grey{fill:var(--band-grey)}
  .brand-mark{fill:var(--ink)}
  .info-l1{font-weight:700;fill:var(--paper)}
  .info-l2{font-weight:600;fill:var(--paper)}
  .info-l3{font-weight:700;fill:var(--paper)}
  .brand-name{font-weight:600;fill:var(--ink)}
  .phone{font-weight:800;fill:var(--ink)}
  .phone-cc{fill:var(--text-grey)}
  .tagline{font-weight:800;fill:var(--paper)}
  .web{font-weight:700;fill:var(--ink)}
  .email{font-weight:500;fill:var(--text-grey)}
  .email-label{font-weight:700;fill:var(--ink)}
  .estimates{font-weight:800;fill:var(--paper)}
</style>
</head>
<body>

<!-- Side view, rear to the left -->
<section class="view view--side-left">
  <svg viewBox="0 0 770 415">
    <rect class="panel" x="36" y="95" width="696" height="257" rx="22"/>
    <polygon class="band-grey" points="48,100 104,95 104,150 258,150 258,158 48,152"/>
    <polygon class="band-dark" points="104,95 268,95 268,120 480,178 730,240 730,280 480,222 440,190 258,150 104,147"/>
    <polygon class="band-grey" points="440,192 480,224 730,282 730,290 478,232 436,198"/>
    <polygon class="band-dark" points="45,230 300,285 560,338 560,352 330,342 45,256"/>
    <polygon class="band-dark" points="262,292 560,330 560,352 262,318"/>

    <text class="info-l1" x="126" y="122" font-size="10">WALLS &amp; FLOOR TILER</text>
    <text class="info-l2" x="126" y="134" font-size="8">DOMESTIC &amp; COMMERCIAL</text>
    <text class="info-l3" x="126" y="144" font-size="5.5">COMPLETE BATHROOM INSTALLATIONS</text>

    <text class="phone" x="252" y="178" font-size="20" textLength="178" lengthAdjust="spacingAndGlyphs" transform="rotate(10 252 178)"><tspan class="phone-cc">+44</tspan> 7700 900318</text>

    <rect class="brand-mark" x="74" y="168" width="58" height="58" transform="rotate(9 103 197)"/>
    <text class="brand-name" x="142" y="222" font-size="32" textLength="200" lengthAdjust="spacingAndGlyphs" transform="rotate(9 142 222)">KELVAN WORK</text>

    <text class="tagline" x="490" y="212" font-size="17" textLength="195" lengthAdjust="spacingAndGlyphs" transform="rotate(13.5 490 212)">WALLS &amp; FLOOR TILER</text>

    <text class="web" x="372" y="250" font-size="16" textLength="195" lengthAdjust="spacingAndGlyphs" transform="rotate(12 372 250)">WWW.KELVANWORK.IE</text>
    <text class="email" x="370" y="268" font-size="11" textLength="190" lengthAdjust="spacingAndGlyphs" transform="rotate(12 370 268)"><tspan class="email-label">EMAIL:</tspan> INFO@KELVANWORK.IE</text>

    <text class="estimates" x="320" y="314" font-size="14" textLength="142" lengthAdjust="spacingAndGlyphs" transform="rotate(7.3 320 314)">FREE ESTIMATES</text>
  </svg>
</section>

<!-- Side view, rear to the right -->
<section class="view view--side-right">
  <svg viewBox="0 0 770 385">
    <rect class="panel" x="38" y="57" width="694" height="253" rx="22"/>
    <polygon class="band-grey" points="665,57 722,62 722,118 665,124"/>
    <polygon class="band-dark" points="505,57 665,57 665,112 520,118 300,180 40,250 40,210 300,150 500,92"/>
    <polygon class="band-grey" points="520,120 300,182 40,252 40,260 300,190 520,128"/>
    <polygon class="band-dark" points="730,190 730,207 505,252 505,240"/>
    <polygon class="band-dark" points="210,290 505,240 505,262 210,315"/>
    <polygon class="band-grey" points="250,320 505,272 505,280 250,328"/>

    <text class="info-l1" x="530" y="80" font-size="10">WALLS &amp; FLOOR TILER</text>
    <text class="info-l2" x="530" y="92" font-size="8">DOMESTIC &amp; COMMERCIAL</text>
    <text class="info-l3" x="530" y="102" font-size="5.5">COMPLETE BATHROOM INSTALLATIONS</text>

    <text class="tagline" x="88" y="228" font-size="17" textLength="205" lengthAdjust="spacingAndGlyphs" transform="rotate(-15 88 228)">WALLS &amp; FLOOR TILER</text>

    <text class="web" x="205" y="258" font-size="16" textLength="200" lengthAdjust="spacingAndGlyphs" transform="rotate(-13.8 205 258)">WWW.KELVANWORK.IE</text>
    <text class="email" x="210" y="273" font-size="11" textLength="195" lengthAdjust="spacingAndGlyphs" transform="rotate(-13.3 210 273)"><tspan class="email-label">EMAIL:</tspan> INFO@KELVANWORK.IE</text>

    <text class="estimates" x="300" y="296" font-size="14" textLength="142" lengthAdjust="spacingAndGlyphs" transform="rotate(-10 300 296)">FREE ESTIMATES</text>

    <rect class="brand-mark" x="434" y="172" width="58" height="58" transform="rotate(-9 463 201)"/>
    <text class="brand-name" x="500" y="218" font-size="32" textLength="200" lengthAdjust="spacingAndGlyphs" transform="rotate(-9 500 218)">KELVAN WORK</text>
  </svg>
</section>

<!-- Front bonnet -->
<section class="view view--front">
  <svg viewBox="0 0 372 400">
    <path class="band-dark" d="M40 140 Q186 112 332 140 L338 235 Q186 248 34 235 Z"/>
    <path class="band-grey" d="M84 148 Q186 132 290 148 L285 232 Q186 240 88 232 Z"/>
    <path class="panel" d="M96 148 Q186 134 276 148 L272 232 Q186 239 100 232 Z"/>
    <rect class="brand-mark" x="129" y="168" width="43" height="43"/>
    <text class="brand-name" x="178" y="187" font-size="17" textLength="62" lengthAdjust="spacingAndGlyphs">KELVAN</text>
    <text class="brand-name" x="178" y="206" font-size="17" textLength="52" lengthAdjust="spacingAndGlyphs">WORK</text>
  </svg>
</section>

<!-- Rear doors -->
<section class="view view--rear">
  <svg viewBox="0 0 396 400">
    <rect class="panel" x="40" y="35" width="322" height="300" rx="16"/>
    <polygon class="band-grey" points="296,35 340,35 320,62 300,68"/>
    <polygon class="band-dark" points="340,35 362,35 362,62 318,72"/>
    <polygon class="band-dark" points="40,134 362,62 362,102 40,174"/>
    <polygon class="band-grey" points="40,178 362,106 362,118 40,190"/>
    <polygon class="band-dark" points="40,290 362,218 362,243 40,315"/>
    <polygon class="band-grey" points="40,320 362,248 362,256 40,328"/>
    <polygon class="band-dark" points="140,335 362,285 362,297 160,335"/>

    <text class="phone" x="62" y="100" font-size="20" textLength="178" lengthAdjust="spacingAndGlyphs" transform="rotate(-12.6 62 100)"><tspan class="phone-cc">+44</tspan> 7700 900318</text>

    <text class="tagline" x="68" y="156" font-size="21" textLength="254" lengthAdjust="spacingAndGlyphs" transform="rotate(-12.7 68 156)">WALLS &amp; FLOOR TILER</text>

    <rect class="brand-mark" x="64" y="182" width="60" height="60" transform="rotate(-12 94 212)"/>
    <text class="brand-name" x="132" y="212" font-size="28" textLength="200" lengthAdjust="spacingAndGlyphs" transform="rotate(-12.4 132 212)">KELVAN WORK</text>

    <text class="web" x="152" y="250" font-size="13" textLength="170" lengthAdjust="spacingAndGlyphs" transform="rotate(-12.4 152 250)">WWW.KELVANWORK.IE</text>

    <text class="estimates" x="72" y="300" font-size="15" textLength="142" lengthAdjust="spacingAndGlyphs" transform="rotate(-12.6 72 300)">FREE ESTIMATES</text>
  </svg>
</section>

<div class="divider divider--h1"></div>
<div class="divider divider--h2"></div>
<div class="divider divider--v"></div>

</body>
</html>
```